Business Card Design

we are a brand new cable TV network devoted to self improvement and leading a better life called FLOURISH TV.I have a logo. We have 3 executives that need cards.I want it to be a heavy stock card: professional but showing our creative nature

Industry/Entity Type

Business

Contact Information for Business Card

CLAUDIA SAENZ AMLIECEO350 San Juan DrPonte Vedra Beach FL 32082904-473-5953

```html
<!DOCTYPE html>
<html lang="en">
<head>
<meta charset="utf-8">
<title>Flourish TV Business Card</title>
<link href="https://fonts.googleapis.com/css2?family=Arimo:wght@400;700&display=swap" rel="stylesheet">
<style>
  :root {
    --page-bg: #e9e6e1;
    --card-bg: #f7f7f7;
    --ink: #1b1b1b;
    --ink-soft: #3a3a3a;
    --brand-red: #8e1519;
    --band-black: #050505;
    --rule: #2a2a2a;
  }
  html, body {
    margin: 0;
    padding: 0;
    width: 1200px;
    height: 902px;
    overflow: hidden;
    background: var(--page-bg);
    font-family: "Arimo", Arial, sans-serif;
  }
  .business-card {
    position: absolute;
    left: 100px;
    top: 165px;
    width: 1000px;
    height: 571px;
    background: var(--card-bg);
    overflow: hidden;
    box-shadow: 0 8px 24px rgba(0,0,0,0.18);
  }
  .brand-name {
    position: absolute;
    left: 100px;
    top: 150px;
    display: flex;
    align-items: center;
    gap: 22px;
    font-weight: 700;
    font-size: 78px;
    letter-spacing: -1px;
    color: var(--ink);
    line-height: 1;
  }
  .brand-mark {
    width: 64px;
    height: 64px;
    background: var(--brand-red);
    border-radius: 8px;
  }
  .divider {
    position: absolute;
    left: 560px;
    top: 230px;
    width: 2px;
    height: 170px;
    background: var(--rule);
  }
  .contact-list {
    position: absolute;
    left: 600px;
    top: 240px;
    margin: 0;
    padding: 0;
    list-style: none;
    font-size: 27px;
    color: var(--ink);
    line-height: 1.25;
  }
  .contact-item {
    display: flex;
    align-items: flex-start;
    gap: 16px;
    margin-bottom: 14px;
  }
  .contact-icon {
    width: 18px;
    height: 18px;
    margin-top: 7px;
    flex: none;
  }
  .person {
    position: absolute;
    left: 100px;
    top: 382px;
    color: var(--ink-soft);
  }
  .person-name {
    margin: 0;
    font-size: 38px;
    font-weight: 400;
  }
  .person-title {
    margin: 8px 0 0 26px;
    font-size: 26px;
    font-weight: 400;
  }
  .card-bands {
    position: absolute;
    left: 0;
    bottom: 0;
    width: 1000px;
    height: 200px;
  }
</style>
</head>
<body>
  <article class="business-card">
    <div class="brand-name"><span class="brand-mark"></span>FLOURISH TV</div>

    <div class="divider"></div>

    <ul class="contact-list">
      <li class="contact-item">
        <svg class="contact-icon" viewBox="0 0 18 18" aria-hidden="true">
          <rect width="18" height="18" rx="2" fill="#1b1b1b"/>
          <path d="M5 4c1 0 1.5 2 1.5 2.6 0 .6-.8.9-.6 1.5.4 1.2 1.6 2.4 2.8 2.8.6.2.9-.6 1.5-.6.6 0 2.6.5 2.6 1.5 0 1-1.2 2-2.2 2C7 13.8 4.2 11 4 6.2 4 5.2 4.2 4 5 4z" fill="#f7f7f7"/>
        </svg>
        <span>555-218-0476</span>
      </li>
      <li class="contact-item">
        <svg class="contact-icon" viewBox="0 0 18 18" aria-hidden="true">
          <rect width="18" height="18" rx="2" fill="#1b1b1b"/>
          <path d="M9 3.5a3.6 3.6 0 0 1 3.6 3.6C12.6 10 9 14.5 9 14.5S5.4 10 5.4 7.1A3.6 3.6 0 0 1 9 3.5z" fill="#f7f7f7"/>
          <circle cx="9" cy="7.1" r="1.3" fill="#1b1b1b"/>
        </svg>
        <span>718 Copper Hollow Ln<br>Alder Cove FL 30915</span>
      </li>
    </ul>

    <div class="person">
      <h1 class="person-name">Marisol Duval Kerno</h1>
      <p class="person-title">CEO</p>
    </div>

    <svg class="card-bands" viewBox="0 0 1000 200" aria-hidden="true">
      <rect x="0" y="100" width="1000" height="100" fill="var(--band-black)"/>
      <path d="M556 200 L556 66 Q556 46 576 45 L1000 22 L1000 200 Z" fill="#f7f7f7"/>
      <path d="M566 200 L566 72 Q566 54 584 53 L1000 30 L1000 200 Z" fill="var(--brand-red)"/>
    </svg>
  </article>
</body>
</html>
```